SLides. Repair phone, tablet, pc, accessories seell and tempered glass.

i would like to show client what we do . what we sell. the repair can be done from 30min. We install tempered glasses. We sell accessories. have already slides. but design not very modern. need to change them. https://files.korvanet.example/share/7QxLm2PzR8TvWc4Hn9Kd https://files.korvanet.example/share/3JfTy6BnQ1XsVe8Ga5Lp i send all the design i have. our website is www.nutiparandus.ee i uploaded what photos i like.

Target Market(s)

Trade buy repair. phones, taböets, PC, sell accessories. show all services

Colors

Designer to choose colors to be used in the design.

Requirements
Must have
• modern design modern phone pictures. zelt pictures vorn pictures. To emphasize our style.
Nice to have
• modern pictures of our services. and modern pictures of goods.
Should not have
• non modern pictures and

```html
<!DOCTYPE html>
<html lang="en">
<head>
<meta charset="utf-8">
<title>Protective Film and Glass Installation Slides</title>
<link rel="stylesheet" href="https://fonts.googleapis.com/css2?family=Montserrat:wght@700&family=Raleway:wght@400;500&display=swap">
<style>
  :root {
    --board: #6b6b6b;
    --navy: #232f36;
    --navy-deep: #1f2a30;
    --teal-mid: #23707f;
    --cyan: #2fbfe0;
    --cyan-bright: #31c3e3;
    --paper: #f3f3f3;
    --white: #ffffff;
    --button-dark: #1d3843;
    --panel-dark: #2c3a41;
  }
  * { margin: 0; padding: 0; box-sizing: border-box; }
  html, body { width: 857px; height: 1200px; overflow: hidden; }
  body { background: var(--board); position: relative; font-family: "Raleway", sans-serif; }

  .slide { position: absolute; left: 55px; width: 742px; height: 353px; overflow: hidden; }
  .slide--gradient { top: 32px; background: linear-gradient(100deg, var(--navy) 0%, var(--navy-deep) 25%, var(--teal-mid) 60%, var(--cyan) 90%, var(--cyan-bright) 100%); }
  .slide--split { top: 416px; background: var(--white); }
  .slide--banner { top: 802px; background: var(--paper); }

  .slide-shape { position: absolute; left: 0; top: 0; width: 742px; height: 353px; }

  .headline { position: absolute; color: var(--white); text-transform: uppercase; }
  .headline--light { left: 52px; top: 77px; font-family: "Raleway", sans-serif; font-weight: 500; font-size: 20.5px; line-height: 21px; letter-spacing: 0.2px; }
  .headline--bold { font-family: "Montserrat", sans-serif; font-weight: 700; font-size: 20px; line-height: 21px; letter-spacing: 0.3px; }

  .feature-list { position: absolute; left: 48px; top: 154px; list-style: none; width: 196px; }
  .feature-list li { position: relative; padding-left: 19px; color: var(--white); font-size: 9.2px; line-height: 11.6px; margin-bottom: 15px; }
  .feature-list li svg { position: absolute; left: 0; top: 3px; width: 14px; height: 14px; }

  .lead { position: absolute; font-size: 11.3px; line-height: 16px; width: 230px; }
  .button { position: absolute; width: 121px; height: 31px; border-radius: 16px; display: flex; align-items: center; justify-content: center; color: var(--white); font-size: 11px; letter-spacing: 0.2px; }
  .button--cyan { background: var(--cyan); }
  .button--dark { background: var(--button-dark); }

  .photo { position: absolute; }
  .photo--parts { left: 316px; top: 52px; width: 401px; height: 247px; background: linear-gradient(90deg, rgba(236,240,242,0.22), rgba(236,240,242,0.30)); }
  .photo--cracked { left: 285px; top: 0; width: 457px; height: 353px; background: linear-gradient(135deg, #ffffff 0%, #f6ede8 55%, #efe3dc 100%); }
  .photo--technician { left: 0; top: 0; width: 742px; height: 353px; background: linear-gradient(160deg, #34434a 0%, var(--panel-dark) 50%, #222d33 100%); clip-path: polygon(0 0, 403px 0, 211px 353px, 0 353px); }
  .photo--layers { left: 425px; top: 47px; width: 253px; height: 251px; background: linear-gradient(180deg, #eef0f1 0%, #e4e7e8 60%, #d9dcde 100%); }
</style>
</head>
<body>

<section class="slide slide--gradient">
  <h2 class="headline headline--light">Protective film and<br>glass professional<br>installation</h2>
  <ul class="feature-list">
    <li><svg viewBox="0 0 14 14"><path d="M1 8 L5 12 L13 1" fill="none" stroke="#2fbfe0" stroke-width="2.4" stroke-linecap="round" stroke-linejoin="round"/></svg>Our store is wide choice of protective film and glasses.</li>
    <li><svg viewBox="0 0 14 14"><path d="M1 8 L5 12 L13 1" fill="none" stroke="#2fbfe0" stroke-width="2.4" stroke-linecap="round" stroke-linejoin="round"/></svg>When buying a protective film or we install it free of charge.</li>
    <li><svg viewBox="0 0 14 14"><path d="M1 8 L5 12 L13 1" fill="none" stroke="#2fbfe0" stroke-width="2.4" stroke-linecap="round" stroke-linejoin="round"/></svg>Coming with your own protection, installation is only 3 C. Installation is not covered by warranty.</li>
  </ul>
  <div class="photo photo--parts" role="img" aria-label="Photo of a smartphone taken apart into four layers: front glass, display with circuit board, mid frame and back cover"></div>
</section>

<section class="slide slide--split">
  <div class="photo photo--cracked" role="img" aria-label="Photo of a hand holding a white smartphone with a shattered screen"></div>
  <div class="photo photo--technician" role="img" aria-label="Dimmed photo of a technician repairing a smartphone"></div>
  <svg class="slide-shape" viewBox="0 0 742 353" aria-hidden="true">
    <polygon points="285,209 211,353 367,353" fill="#2fbfe0"/>
  </svg>
  <h2 class="headline headline--bold" style="left:57px; top:88px;">Protective film and<br>glass professional<br>installation</h2>
  <p class="lead" style="left:56px; top:159px; color:var(--white);">We provide professional protection installation. When buying a protective film or we install it free of charge.</p>
  <div class="button button--cyan" style="left:56px; top:216px;">LEARN MORE</div>
</section>

<section class="slide slide--banner">
  <div class="photo photo--layers" role="img" aria-label="Illustration of a smartphone with layered protective film and tempered glass floating above the screen"></div>
  <svg class="slide-shape" viewBox="0 0 742 353" aria-hidden="true">
    <polygon points="0,60 304,60 391,165 304,269 0,269" fill="#31c0e1"/>
  </svg>
  <h2 class="headline headline--bold" style="left:54px; top:93px;">Protective film and<br>glass professional<br>installation</h2>
  <p class="lead" style="left:54px; top:162px; color:var(--white);">We provide professional protection installation. When buying a protective film or we install it free of charge.</p>
  <div class="button button--dark" style="left:54px; top:218px;">LEARN MORE</div>
</section>

</body>
</html>
```